Re-design my 1-page website to be BETTER!

Hi Guys,
I recently created a 1-page website for market testing purposes for a company I am starting. Problem is, the feedback i've had on the page is its a bit corporate and boring.
I would love you to design something that is fresher, more modern and will generate leads (via the sign up CTA's).
Here is the website as it is now: www.guidelinkhub.com.au.
If you need any info or have questions, just reach out.
Thanks,
Oliver

Target Market(s)

Entrepreneurs

Number of Pages Required

1 page

Font styles to use
Sans Serif

Colors
abd036
34a6d7
ffffff

Requirements
Must have
• Fresh, Modern, high-converting
• I expect 70% of traffic to be mobile so must be mobile optimised first.
Nice to have
• I've highlighted colours i like below, however, I am open to suggestions. I like colours that are gender neutral and show energy and vibrancy.
• I have used Proxima Nova for the fonts, as I find it easy to read however, I am open to suggestions. My main preference is that it displays well and is easily read

```html
<!DOCTYPE html>
<html lang="en">
<head>
<meta charset="utf-8">
<title>GuideLink Hub – A Mentor For Everyone</title>
<link href="https://fonts.googleapis.com/css2?family=Montserrat:wght@400;600;700&family=Open+Sans:ital,wght@0,400;0,600;0,700;1,400&display=swap" rel="stylesheet">
<style>
:root{
  --blue:#13399a;
  --blue-dark:#0d2d80;
  --green:#41c80e;
  --green-dark:#33a80a;
  --grey-bg:#d9d9d9;
  --light-bg:#efefef;
  --text:#333;
  --white:#fff;
  --black:#000;
}
*{box-sizing:border-box;margin:0;padding:0}
html,body{width:1200px;height:4054px;overflow:hidden}
body{font-family:"Open Sans",Arial,sans-serif;color:var(--text);background:var(--white)}
section,header,footer{position:relative;width:1200px}
.abs{position:absolute}
h1,h2,h3,.brand{font-family:"Montserrat",Arial,sans-serif}
.green{color:var(--green)}

/* header */
.top-strip{height:11px;background:var(--blue)}
.site-header{height:119px;background:var(--white)}
.brand{font-weight:700;font-size:36px;color:var(--blue);left:76px;top:34px;line-height:1}
.tagline{left:78px;top:76px;font-size:15px;color:var(--text)}
.phone{left:750px;top:36px;font-size:18px;color:var(--blue);display:flex;align-items:center;gap:8px}
.follow{left:935px;top:38px;font-size:17px;font-weight:700;color:var(--blue)}
.social{left:1040px;top:39px;display:flex;gap:4px}
.social span{width:16px;height:16px;background:#888;display:block}
.nav{left:514px;top:88px;display:flex;font-size:14px;color:#444}
.nav a{color:inherit;text-decoration:none;padding:0 8px;border-right:1px solid #bbb;line-height:1}
.nav a:last-child{border:none}
.nav a.active{color:var(--blue);font-weight:700}

/* hero */
.hero{height:573px;background:linear-gradient(100deg,#6d7780 0%,#a7adb3 40%,#c9c4bd 65%,#8d8e8c 100%)}
.hero-title{left:134px;top:318px;font-size:66px;font-weight:700;color:var(--blue)}
.hero-text{left:130px;top:400px;width:500px;font-size:17px;line-height:26px;color:var(--white)}
.btn{display:inline-block;font-family:"Open Sans",Arial,sans-serif;text-transform:uppercase;text-decoration:none;color:var(--white)}
.hero-btn{left:122px;top:502px;width:135px;height:42px;line-height:42px;text-align:center;background:var(--blue);border-radius:22px;font-size:14px}
.arrow{top:400px;color:rgba(255,255,255,.8);font-size:60px;line-height:1}

/* features */
.features{height:608px;background:var(--grey-bg)}
.section-title{width:1200px;text-align:center;font-weight:700;font-size:42px;color:var(--blue)}
.card{top:162px;width:284px;height:384px;background:var(--white);border-bottom:8px solid var(--green);text-align:center;padding:0 26px}
.card-icon{margin:34px auto 0;width:124px;height:124px;border-radius:50%;background:var(--green);display:flex;align-items:center;justify-content:center}
.card h3{margin-top:52px;font-size:15px;color:var(--blue);font-weight:700}
.card p{margin-top:14px;font-size:13px;line-height:22px;color:#333}

/* about */
.about{height:622px;background:var(--green);color:var(--white)}
.about .section-title{top:50px}
.about-lead{left:150px;top:146px;width:900px;text-align:center;font-size:12px;line-height:22px}
.about-sub{left:127px;top:252px;font-size:26px;font-weight:400;font-family:"Open Sans",Arial,sans-serif}
.about-text{left:127px;top:312px;width:440px;font-size:12.5px;line-height:22px}
.about-btn{left:127px;top:482px;width:130px;height:30px;line-height:30px;text-align:center;background:var(--blue);font-size:13px}
.about-photo{left:622px;top:249px;width:451px;height:302px;border:4px solid var(--blue);background:linear-gradient(120deg,#5f6468,#a9acae 45%,#40464c)}

/* benefits */
.benefits{height:670px;background:var(--light-bg)}
.benefits .section-title{top:56px}
.benefits-sub{width:1200px;top:112px;text-align:center;font-style:italic;font-size:28px;color:var(--blue)}
.rule{left:560px;top:160px;width:80px;height:2px;background:var(--green)}
.benefit{top:225px;width:220px;text-align:center}
.benefit-photo{width:216px;height:216px;border-radius:50%;border:4px solid var(--white);margin:0 auto;background:linear-gradient(135deg,#8b8f94,#c7c3bd 55%,#5c6168)}
.benefit h3{margin-top:24px;font-size:24px;font-weight:600;color:var(--green);font-family:"Open Sans",Arial,sans-serif}
.more-btn{left:516px;top:575px;width:152px;height:38px;line-height:38px;text-align:center;background:var(--green);font-size:11px;font-weight:600}

/* stories */
.stories{height:411px;background:var(--blue)}
.stories .section-title{top:50px;color:var(--white)}
.story{top:142px;width:325px}
.avatar{width:54px;height:54px;border-radius:50%;border:3px solid var(--white);background:linear-gradient(135deg,#777,#bbb);float:left}
.story-meta{margin-left:70px;color:var(--white);padding-top:4px}
.story-meta strong{font-size:12px;display:block;font-family:"Montserrat",Arial,sans-serif}
.story-meta span{font-size:9.5px;display:block;line-height:16px}
.story-box{position:absolute;top:80px;width:325px;height:121px;background:var(--green);color:var(--white);font-size:12px;line-height:21px;padding:16px 24px}
.story-box::before{content:"";position:absolute;top:-10px;left:26px;border:10px solid transparent;border-top:0;border-bottom-color:var(--green)}

/* faq */
.faq{height:554px;background:var(--light-bg)}
.faq .section-title{top:48px;font-family:"Open Sans",Arial,sans-serif}
.q{width:511px;height:38px;border:2px solid #8a8a8a;background:var(--white);display:flex;align-items:center;padding:0 14px;font-size:16px;font-weight:600;color:#333;text-transform:uppercase}
.q b{color:var(--blue);margin-right:8px}
.q i{margin-left:auto;font-style:normal;color:var(--blue);font-size:20px}
.q.open{background:var(--blue);color:var(--white);border-color:var(--blue);width:508px}
.q.open b{color:var(--white)}
.answer{left:641px;top:197px;width:508px;height:120px;background:#a9a9a9;color:var(--white);font-size:12px;line-height:20px;padding:14px 14px}

/* cta */
.cta{height:70px;background:var(--green)}
.cta-text{left:186px;top:18px;font-size:28px;font-weight:700;color:var(--white);font-family:"Montserrat",Arial,sans-serif}
.cta-btn{left:730px;top:12px;width:195px;height:46px;line-height:46px;text-align:center;background:var(--blue);border-radius:14px;font-size:22px;font-weight:700}

/* footer */
.site-footer{height:335px;background:var(--black);color:var(--white)}
.foot-brand{left:95px;top:94px;font-size:20px;color:var(--blue)}
.foot-tag{left:96px;top:118px;font-size:10px}
.foot-text{left:95px;top:168px;width:220px;font-size:11px;line-height:18px;color:#ccc}
.foot-head{top:86px;font-size:16px;font-family:"Open Sans",Arial,sans-serif;font-weight:400;letter-spacing:.5px}
.contact-line{left:343px;display:flex;gap:14px;font-size:13px;line-height:18px}
.links{left:614px;top:132px;list-style:none;font-size:13px;line-height:33px}
.field{height:38px;background:var(--white);color:#666;font-size:12px;padding:0 8px;line-height:38px}
.send{left:819px;top:245px;width:134px;height:34px;line-height:34px;text-align:center;background:var(--green);font-size:14px;font-weight:700}
.copyright{height:81px;background:var(--blue);color:#cfd8f0;font-size:12px;text-align:center;line-height:81px}
</style>
</head>
<body>

<div class="top-strip"></div>
<header class="site-header">
  <div class="abs brand">GuideLink Hub</div>
  <div class="abs tagline">A Mentor For Everyone</div>
  <div class="abs phone">
    <svg width="18" height="18" viewBox="0 0 24 24"><path fill="#13399a" d="M6.6 10.8a15 15 0 0 0 6.6 6.6l2.2-2.2a1 1 0 0 1 1-.25 11.4 11.4 0 0 0 3.6.6 1 1 0 0 1 1 1V20a1 1 0 0 1-1 1A17 17 0 0 1 3 4a1 1 0 0 1 1-1h3.5a1 1 0 0 1 1 1c0 1.25.2 2.45.6 3.6a1 1 0 0 1-.25 1z"/></svg>
    (555) 274 0193
  </div>
  <div class="abs follow">Follow Us</div>
  <div class="abs social"><span></span><span></span><span></span><span></span></div>
  <nav class="abs nav">
    <a class="active" href="#">HOME</a><a href="#">ABOUTUS</a><a href="#">SERVICES</a><a href="#">HOW IT WORKS</a><a href="#">NEWS</a><a href="#">FAQS</a><a href="#">CONTACT US</a>
  </nav>
</header>

<section class="hero" role="img" aria-label="Photo of a smiling professional woman in an office">
  <h1 class="abs hero-title">GuideLink <span class="green">Hub</span></h1>
  <p class="abs hero-text">consectetuer adipiscing elit. Aenean commodo ligula eget dolor. Aenean massa. Cum sociis natoque penatibus et magnis dis parturient montes.</p>
  <a class="abs btn hero-btn" href="#">Read more</a>
  <div class="abs arrow" style="left:50px">&#8249;</div>
  <div class="abs arrow" style="left:1115px">&#8250;</div>
</section>

<section class="features">
  <h2 class="abs section-title" style="top:64px">Mentorship : <span class="green">But Different</span></h2>
  <div class="abs card" style="left:65px">
    <div class="card-icon"><svg width="64" height="64" viewBox="0 0 64 64"><path fill="none" stroke="#fff" stroke-width="4" d="M10 14h44v28H30l-12 10V42h-8z"/><circle cx="22" cy="28" r="3" fill="#fff"/><circle cx="32" cy="28" r="3" fill="#fff"/><circle cx="42" cy="28" r="3" fill="#fff"/></svg></div>
    <h3>TELL US WHAT YOU NEED</h3>
    <p>There is no one size fits all approach to Mentorship. So tell us the challenges you are facing and the skill-set your Mentor must have.</p>
  </div>
  <div class="abs card" style="left:451px">
    <div class="card-icon"><svg width="64" height="64" viewBox="0 0 64 64"><path fill="none" stroke="#fff" stroke-width="4" stroke-linecap="round" stroke-linejoin="round" d="M22 14l8 8 14-14"/><rect x="8" y="32" width="14" height="20" fill="none" stroke="#fff" stroke-width="4"/><rect x="25" y="28" width="14" height="24" fill="none" stroke="#fff" stroke-width="4"/><rect x="42" y="32" width="14" height="20" fill="none" stroke="#fff" stroke-width="4"/></svg></div>
    <h3>CHOOSE YOUR MENTOR</h3>
    <p>Mentors are invited to Mentor you. We select 3 top picks that align with your criteria. It's then up to you whether you choose a Mentor, interview 1 or more or refine your criteria and start again.</p>
  </div>
  <div class="abs card" style="left:846px">
    <div class="card-icon"><svg width="64" height="64" viewBox="0 0 64 64"><path fill="none" stroke="#fff" stroke-width="4" stroke-linecap="round" d="M50 26a18 18 0 0 0-32-8M14 38a18 18 0 0 0 32 8"/><path fill="#fff" d="M16 8v12h12zM48 56V44H36z"/></svg></div>
    <h3>ONGOING SUPPORT</h3>
    <p>We don't stop once you have your perfect Mentor. We're on hand to make life easy for you, keep your sessions on track and provide ongoing support</p>
  </div>
</section>

<section class="about">
  <h2 class="abs section-title" style="color:var(--blue)">About us</h2>
  <p class="abs about-lead">Lorem ipsum dolor sit amet, consectetur adipiscing elit. Quid autem habent admirationis, cum prope accessoris? An hoc usque quaque, aliter in vita? Non igitur de improbo, sed de callido improbo quaerimus, qualis Q. Nam quibusdam efficiuntur voluptates, eas non sunt in potestate sapientis.</p>
  <h3 class="abs about-sub">Lorem ipsum dolor sit amet</h3>
  <p class="abs about-text">Lorem ipsum dolor sit amet, consectetur adipiscing elit. Quid autem habent admirationis, cum prope accessoris? An hoc usque quaque, aliter in vita? Non igitur de improbo, sed de callido improbo quaerimus, qualis Q. Nam quibus rebus efficiuntur voluptates, eae non sunt in potestate sapientis proprium desperationem sapientiae. Illi propter opem vivere. Quid enim me prohiberet Epicureum esse, si probarem, quae ille diceret? Qui vero falsum, quaerere mittimus dolor oculis et privatio.</p>
  <a class="abs btn about-btn" href="#">Read more &nbsp;&#8250;</a>
  <div class="abs about-photo" role="img" aria-label="Photo of a smiling businesswoman in a meeting room with colleagues"></div>
</section>

<section class="benefits">
  <h2 class="abs section-title">How a Mentor</h2>
  <p class="abs benefits-sub">Will Accelerate Your Growth</p>
  <div class="abs rule"></div>
  <div class="abs benefit" style="left:74px"><div class="benefit-photo" role="img" aria-label="Photo of two people discussing documents at a desk"></div><h3>Impartial advice</h3></div>
  <div class="abs benefit" style="left:344px"><div class="benefit-photo" role="img" aria-label="Photo of a smiling young man in a casual jacket"></div><h3>Avoid the Pitfalls</h3></div>
  <div class="abs benefit" style="left:614px"><div class="benefit-photo" role="img" aria-label="Photo of two businessmen talking"></div><h3>A Supportive Ear</h3></div>
  <div class="abs benefit" style="left:885px"><div class="benefit-photo" role="img" aria-label="Photo of a businessman standing in a bright office"></div><h3>Clarity</h3></div>
  <a class="abs btn more-btn" href="#">More service</a>
</section>

<section class="stories">
  <h2 class="abs section-title">Sucessfull <span class="green">Stories</span></h2>
  <div class="abs story" style="left:89px">
    <div class="avatar" role="img" aria-label="Portrait photo of client"></div>
    <div class="story-meta"><strong>MR HALDEN</strong><span>President of Northgate Advisory Group</span><span>Senior adviser partner</span></div>
    <div class="story-box">Lorem ipsum dolor sit amet, consectetur adipiscing elit. Quid autem habent admirationis, cum prope accessoris? An hoc usque quaque, aliter in vita?</div>
  </div>
  <div class="abs story" style="left:438px">
    <div class="avatar" role="img" aria-label="Portrait photo of client"></div>
    <div class="story-meta"><strong>MR CARVER</strong><span>President of Northgate Advisory Group</span><span>Senior adviser partner</span></div>
    <div class="story-box">Lorem ipsum dolor sit amet, consectetur adipiscing elit. Quid autem habent admirationis, cum prope accessoris? An hoc usque quaque, aliter in vita?</div>
  </div>
  <div class="abs story" style="left:784px">
    <div class="avatar" role="img" aria-label="Portrait photo of client"></div>
    <div class="story-meta"><strong>MR PELLMAN</strong><span>President of Northgate Advisory Group</span><span>Senior adviser partner</span></div>
    <div class="story-box">Lorem ipsum dolor sit amet, consectetur adipiscing elit. Quid autem habent admirationis, cum prope accessoris? An hoc usque quaque, aliter in vita?</div>
  </div>
</section>

<section class="faq">
  <h2 class="abs section-title">FAQ'S</h2>
  <div class="abs q" style="left:89px;top:178px"><b>Q: 1</b> What is a mentor?<i>+</i></div>
  <div class="abs q" style="left:89px;top:240px"><b>Q: 2</b> Is a mentor right for me?<i>+</i></div>
  <div class="abs q" style="left:89px;top:308px"><b>Q: 3</b> How often do we meet?<i>+</i></div>
  <div class="abs q" style="left:89px;top:370px"><b>Q: 4</b> Can I have more than one mentor?<i>+</i></div>
  <div class="abs q" style="left:89px;top:435px"><b>Q: 5</b> What if it doesn't work out?<i>+</i></div>
  <div class="abs q open" style="left:641px;top:159px"><b>6</b> How do we meet?</div>
  <p class="abs answer">The Power of GuideLink Hub is you are selecting Mentors from a global pool, not just your immediate network.<br><br>This means that face to face meetings are often not possible, in which case we recommend a video call.</p>
  <div class="abs q" style="left:641px;top:349px;width:508px"><b>Q: 7</b> What are the costs?<i>+</i></div>
</section>

<section class="cta">
  <div class="abs cta-text">ARE YOU READY FOR COACHING?</div>
  <a class="abs btn cta-btn" href="#">GET READY?</a>
</section>

<footer class="site-footer">
  <div class="abs brand foot-brand">GuideLink Hub</div>
  <div class="abs foot-tag">A Mentor For Everyone</div>
  <p class="abs foot-text">Lorem ipsum dolor sit amet, consectetur adipiscing elit. Morbi auctor ullamcorper congue. Phasellus quis lacus quis ante ornare tincidunt lobortis quisquam.</p>

  <h3 class="abs foot-head" style="left:343px">CONTACT US</h3>
  <div class="abs contact-line" style="top:130px"><svg width="16" height="20" viewBox="0 0 16 20"><path fill="#fff" d="M8 0a8 8 0 0 0-8 8c0 6 8 12 8 12s8-6 8-12a8 8 0 0 0-8-8zm0 11a3 3 0 1 1 0-6 3 3 0 0 1 0 6z"/></svg><span>48 Harbour Lane<br>Suite 12<br>Fairview, CA 90210</span></div>
  <div class="abs contact-line" style="top:212px"><svg width="16" height="16" viewBox="0 0 24 24"><path fill="#fff" d="M6.6 10.8a15 15 0 0 0 6.6 6.6l2.2-2.2a1 1 0 0 1 1-.25 11.4 11.4 0 0 0 3.6.6 1 1 0 0 1 1 1V20a1 1 0 0 1-1 1A17 17 0 0 1 3 4a1 1 0 0 1 1-1h3.5a1 1 0 0 1 1 1c0 1.25.2 2.45.6 3.6a1 1 0 0 1-.25 1z"/></svg><span>(555) 274 0193</span></div>
  <div class="abs contact-line" style="top:238px"><svg width="16" height="14" viewBox="0 0 16 12"><rect width="16" height="12" fill="#fff"/><path d="M0 0l8 6 8-6" fill="none" stroke="#000" stroke-width="1.5"/></svg><span>hello@guidelinkhub.com</span></div>

  <h3 class="abs foot-head" style="left:614px">ABOUT US</h3>
  <ul class="abs links"><li>Home</li><li>Services</li><li>News</li><li>Contact Us</li></ul>

  <h3 class="abs foot-head" style="left:819px">GET IN TOUCH</h3>
  <div class="abs field" style="left:819px;top:128px;width:144px">Name</div>
  <div class="abs field" style="left:971px;top:128px;width:144px">Phone</div>
  <div class="abs field" style="left:819px;top:182px;width:296px">Email address</div>
  <a class="abs btn send" href="#">SEND</a>
</footer>
<div class="copyright">Copyright © 2017 guidelinkhub - All Rights Reserved</div>

</body>
</html>
```